Box Design of "pet rapid test for dogs & cats" with professional use

"The market is in Southeast Asia, South America, Europe, and the U.S."
Clients: Veterinary clinics, pet hospitals,(a small number of home use)

Primary colors:
Orange, Green,or Blue, (select 1,or 2 color)
Neutrals: Black, Gray, or White (optional)
Dimensions:135mm(L)*90mm(W)*105mm(W)

Kindly review the attached file for additional content
Updates

I have increased my budget, please provide a satisfactory design solution, thank you very much for your work.

Target Market(s)

Southeast Asia, South America, Europe, and the U.S.

Industry/Entity Type

Veterinary test kit for dogs & cats

Colors
0054AA
0677BA
7BADD7
CADEEF
E8F1F8
0094D4
00A9DD
6FCCEA
C7EBF8
E9F6FB
00AB8E
00BBA5
67D7C9
C6EFE9
E9F9F6
59FF00
82FF00
B8FF75
E3FFCB
F4FFEA
F0912C
F2A743
F7CA91
FBE8D2
FDF5EE
EE7325
F08F49
F5BC92
FAE3D3
FDF4ED

Requirements
Nice to have
• Appealing Box Appearance with professional

```html
<!DOCTYPE html>
<html lang="es">
<head>
<meta charset="utf-8">
<title>Vetluma – Kit de prueba rápida</title>
<link rel="stylesheet" href="https://fonts.googleapis.com/css2?family=Montserrat:wght@400;600;800&family=Roboto:wght@400;500&family=Roboto+Condensed:wght@400;600&display=swap">
<style>
  :root{
    --bg:#e4e4e4;
    --panel:#efefef;
    --blue:#2f6496;
    --blue-deep:#285b8c;
    --blue-soft:#6179a2;
    --ink:#2f5f93;
    --ink-light:#4f73a5;
    --white:#ffffff;
  }
  html,body{margin:0;padding:0;width:1200px;height:1200px;overflow:hidden;background:var(--bg);}
  .canvas{position:relative;width:1200px;height:1200px;}
  .panel{position:absolute;top:320px;height:560px;background:var(--panel);overflow:hidden;box-shadow:0 2px 10px rgba(0,0,0,.08);}
  .front{left:50px;width:760px;}
  .side{left:820px;width:330px;}

  .band-light{position:absolute;left:0;right:0;top:372px;height:36px;background:var(--blue-soft);}
  .band-pattern{position:absolute;left:0;right:0;top:408px;height:112px;background:linear-gradient(180deg,var(--blue) 0%,var(--blue-deep) 100%);}

  .brand{position:absolute;left:60px;top:60px;display:flex;align-items:flex-start;gap:14px;}
  .brand-square{width:62px;height:62px;border-radius:10px;background:var(--ink);}
  .brand-name{font-family:'Montserrat',sans-serif;font-weight:800;font-size:30px;line-height:1;color:var(--ink);letter-spacing:.5px;margin-top:4px;}
  .brand-tagline{font-family:'Montserrat',sans-serif;font-weight:400;font-size:8.5px;line-height:1.2;color:var(--ink);margin-top:8px;}

  .title{position:absolute;left:60px;top:150px;font-family:'Montserrat',sans-serif;color:var(--ink);}
  .title-main{font-size:44px;line-height:1;margin:0;}
  .title-main b{font-weight:800;}
  .title-main span{font-weight:400;color:var(--ink-light);}
  .title-sub{font-size:22px;font-weight:600;margin:6px 0 0;letter-spacing:.3px;}
  .title-species{font-size:20px;font-weight:400;color:var(--ink-light);margin:4px 0 0;}

  .contents{position:absolute;left:60px;top:272px;font-family:'Roboto',sans-serif;font-size:16px;color:var(--ink);line-height:1.9;}
  .contents .row{display:flex;gap:22px;}

  .count-tab{position:absolute;left:90px;top:408px;width:240px;height:48px;background:var(--blue-soft);clip-path:polygon(0 0,100% 0,94% 100%,4% 100%);color:var(--white);font-family:'Montserrat',sans-serif;display:flex;align-items:center;justify-content:center;gap:6px;}
  .count-num{font-weight:800;font-size:22px;}
  .count-label{font-weight:600;font-size:13px;letter-spacing:1px;line-height:1;}
  .count-label small{display:block;font-size:7px;letter-spacing:5px;font-weight:400;}

  .symbols{position:absolute;left:488px;top:322px;display:flex;align-items:center;gap:12px;color:var(--ink);}
  .ivd{font-family:'Roboto',sans-serif;font-weight:500;font-size:18px;border:2px solid var(--ink);padding:2px 7px;}

  .side-brand{position:absolute;left:0;top:40px;width:120px;height:64px;background:var(--blue);color:var(--white);font-family:'Roboto Condensed',sans-serif;padding:10px 0 0 18px;box-sizing:border-box;}
  .side-brand strong{display:block;font-size:15px;font-weight:600;}
  .side-brand em{font-style:normal;font-size:6px;letter-spacing:.5px;}
  .features{position:absolute;left:18px;top:118px;right:14px;margin:0;padding:0;list-style:none;font-family:'Roboto Condensed',sans-serif;font-size:11px;line-height:1.4;color:var(--ink);}
  .features .head{font-weight:600;}
  .features .head::before{content:"";display:inline-block;width:6px;height:9px;background:var(--ink);margin-right:6px;}
  .features .item::before{content:"✓ ";font-size:9px;}
  .maker{position:absolute;right:16px;top:470px;text-align:right;font-family:'Roboto Condensed',sans-serif;color:var(--white);font-size:10px;line-height:1.4;}
  .maker small{font-size:6px;letter-spacing:1px;opacity:.8;}
</style>
</head>
<body>
<div class="canvas">

  <section class="panel front">
    <div class="band-light"></div>
    <div class="band-pattern" role="img" aria-label="Patrón suave de huellas de mascota en tonos azules"></div>

    <div class="brand">
      <div class="brand-square"></div>
      <div>
        <div class="brand-name">VETLUMA</div>
        <div class="brand-tagline">QUERIDO POR LAS MASCOTAS,<br>CONFIADO POR VETERINARIOS</div>
      </div>
    </div>

    <div class="title">
      <p class="title-main"><b>KIT DE</b> <span>PRUEBA</span></p>
      <p class="title-sub">RÁPIDA PARA MASCOTAS</p>
      <p class="title-species">PERROS Y GATOS</p>
    </div>

    <div class="contents">
      <div>(1)- Kits de prueba (cassette, gotero desechable, desecante)</div>
      <div class="row"><span>(2)- Buffer de ensayo</span><span>(4)- Manual de instrucciones</span></div>
      <div class="row"><span>(3)- Hisopos estériles</span><span>(5)- Almacenamiento: 2~30°C</span></div>
    </div>

    <div class="symbols">
      <span class="ivd">IVD</span>
      <svg width="42" height="44" viewBox="0 0 46 48" aria-label="Límite de temperatura 2–30 °C">
        <line x1="22" y1="6" x2="22" y2="40" stroke="#2f5f93" stroke-width="3"/>
        <circle cx="22" cy="42" r="4" fill="#2f5f93"/>
        <path d="M22 8 H30 M14 32 H22" stroke="#2f5f93" stroke-width="1.5"/>
        <text x="31" y="10" font-size="8" fill="#2f5f93" font-family="Roboto,sans-serif">30°C</text>
        <text x="0" y="34" font-size="8" fill="#2f5f93" font-family="Roboto,sans-serif">2°C</text>
      </svg>
      <svg width="36" height="40" viewBox="0 0 40 44" aria-label="Proteger de la luz solar">
        <circle cx="20" cy="14" r="5" fill="none" stroke="#2f5f93" stroke-width="2"/>
        <g stroke="#2f5f93" stroke-width="1.5">
          <line x1="20" y1="2" x2="20" y2="6"/><line x1="8" y1="14" x2="12" y2="14"/><line x1="28" y1="14" x2="32" y2="14"/>
          <line x1="11" y1="5" x2="14" y2="8"/><line x1="29" y1="5" x2="26" y2="8"/>
        </g>
        <path d="M8 32 L20 22 L32 32" fill="none" stroke="#2f5f93" stroke-width="2.5"/>
        <rect x="15" y="32" width="10" height="10" fill="#2f5f93"/>
      </svg>
      <svg width="36" height="31" viewBox="0 0 40 34" aria-label="Consultar instrucciones de uso">
        <path d="M2 4 L18 8 L18 32 L2 28 Z M38 4 L22 8 L22 32 L38 28 Z" fill="none" stroke="#2f5f93" stroke-width="2"/>
        <text x="26" y="26" font-size="16" font-weight="700" fill="#2f5f93" font-family="Roboto,sans-serif">i</text>
      </svg>
      <svg width="38" height="38" viewBox="0 0 44 44" aria-label="No reutilizar">
        <circle cx="22" cy="22" r="19" fill="none" stroke="#2f5f93" stroke-width="2.5"/>
        <line x1="9" y1="9" x2="35" y2="35" stroke="#2f5f93" stroke-width="2.5"/>
        <text x="14" y="30" font-size="22" fill="#2f5f93" font-family="Roboto,sans-serif">2</text>
      </svg>
    </div>

    <div class="count-tab">
      <span class="count-num">10</span>
      <span class="count-label">PRUEBAS<small>POR CAJA</small></span>
    </div>
  </section>

  <section class="panel side">
    <div class="band-light"></div>
    <div class="band-pattern" role="img" aria-label="Patrón suave de huellas de mascota en tonos azules"></div>

    <div class="side-brand"><strong>VETLUMA</strong><em>RAPID TEST KIT</em></div>

    <ul class="features">
      <li class="head">Fácil y Práctico:</li>
      <li class="item">Sin capacitación previa</li>
      <li class="item">Suficientemente simple para uso en casa</li>
      <li class="head">RÁPIDO Y EFICIENTE:</li>
      <li class="item">Resultados digitales en &lt;10 minutos</li>
      <li class="item">Desde inicio hasta resultado final</li>
      <li class="head">PRECISO Y FIABLE:</li>
      <li class="item">Resultados rápidos y confiables con tecnología de inmunocromatografía avanzada</li>
      <li class="item">Validado por clínicas veterinarias a nivel global</li>
      <li class="head">DETECCIÓN MULTIENFERMEDADES:</li>
      <li class="item">Evalúa múltiples patologías simultáneamente</li>
      <li class="item">Ayuda a los dueños a detectar problemas a tiempo</li>
    </ul>

    <div class="maker">MADE by NORVET<br><small>LOVED BY PETS, TRUSTED BY VETS</small></div>
  </section>

</div>
</body>
</html>
```